Construction material supplies company business card ****

1. Full company name “K R Mortar Works Ltd”
I am after a Business card design for the company as a whole. We are better known in Solomon Islands as “K R Mortar” for short.

We are a building materials supplier of
Ready Mixed Concrete, Bricks and Blocks,
Quarry products- gravel, aggregates, sand etc.
Cement distributor/retailer of reputable brands.
Other prefab concrete products. Culverts, wave breakers, concrete retaining blocks etc.

2. Competitive Advantage over Competition: Quality, efficient, professional, dependable, reliable

3. We want people to feel trust worthy, high quality, strong when they see our brand

5. No preference to color. Maybe more sturdy and corporate. Not fancy.

Industry/Entity Type

CONSTRUCTION SUPPLY

Contact Information for Business Card

Name, Position, office phone mob phone, email

Requirements
Must have
• the company logo
Nice to have
• would like to see a mixture of designs, of with logo only and also with simple graphic designs to bring out the company whilst still have the strong sturdy professional feeling

```html
<!DOCTYPE html>
<html lang="en">
<head>
<meta charset="utf-8">
<title>K R Mortar – Business Card</title>
<link rel="stylesheet" href="https://fonts.googleapis.com/css2?family=Arimo:wght@400;700&display=swap">
<style>
  :root {
    --page: #e9e8e6;
    --card: #1c4569;
    --ink: #ffffff;
    --rule: rgba(255,255,255,0.75);
    --shadow: rgba(0,0,0,0.28);
  }
  * { box-sizing: border-box; margin: 0; padding: 0; }
  html, body {
    width: 1200px; height: 801px; overflow: hidden;
    background: var(--page);
    font-family: "Arimo", Arial, sans-serif;
    color: var(--ink);
  }
  .sheet {
    position: relative; width: 1200px; height: 801px;
    display: flex; align-items: center; justify-content: center; gap: 40px;
  }
  .card {
    position: relative; width: 540px; height: 309px;
    background: var(--card);
    box-shadow: 0 10px 24px var(--shadow);
  }

  /* Front: contact side */
  .brand {
    position: absolute; left: 40px; top: 58px;
    display: flex; align-items: center; gap: 12px;
  }
  .brand-square { width: 18px; height: 18px; background: var(--ink); }
  .brand-name {
    font-weight: 700; font-size: 34px; letter-spacing: 2px; text-transform: uppercase;
    white-space: nowrap;
  }
  .person { position: absolute; left: 40px; top: 150px; }
  .person-name { font-weight: 700; font-size: 20px; letter-spacing: 1px; text-transform: uppercase; white-space: nowrap; }
  .person-role { font-size: 14px; margin-top: 4px; }
  .divider {
    position: absolute; left: 262px; top: 132px; width: 1px; height: 76px; background: var(--rule);
  }
  .contacts {
    position: absolute; left: 284px; top: 130px; list-style: none;
    font-size: 14px; line-height: 27px; white-space: nowrap;
  }
  .contacts li { display: flex; align-items: center; gap: 10px; }
  .contacts svg { width: 14px; height: 14px; fill: var(--ink); flex: none; }
  .address {
    position: absolute; left: 40px; bottom: 36px; font-size: 14px;
  }

  /* Back: services side */
  .back { display: flex; flex-direction: column; align-items: center; justify-content: center; }
  .back .brand { position: static; gap: 16px; margin-bottom: 40px; }
  .back .brand-square { width: 26px; height: 26px; }
  .back .brand-name { font-size: 46px; letter-spacing: 3px; }
  .services {
    list-style: none; display: flex; flex-wrap: wrap; justify-content: center;
    gap: 6px 16px; width: 470px; font-size: 15px; text-transform: uppercase;
  }
  .services li { display: flex; align-items: center; gap: 7px; white-space: nowrap; }
  .services li::before {
    content: ""; width: 10px; height: 10px; background: var(--ink); border-radius: 2px;
  }
</style>
</head>
<body>
<main class="sheet">
  <section class="card front">
    <div class="brand">
      <span class="brand-square"></span>
      <span class="brand-name">K R Mortar</span>
    </div>
    <div class="person">
      <p class="person-name">Daniel Harper</p>
      <p class="person-role">Manager</p>
    </div>
    <div class="divider"></div>
    <ul class="contacts">
      <li>
        <svg viewBox="0 0 24 24" aria-hidden="true"><path d="M6.6 10.8a15.1 15.1 0 0 0 6.6 6.6l2.2-2.2a1 1 0 0 1 1-.25 11.4 11.4 0 0 0 3.6.57 1 1 0 0 1 1 1V20a1 1 0 0 1-1 1A17 17 0 0 1 3 4a1 1 0 0 1 1-1h3.5a1 1 0 0 1 1 1c0 1.25.2 2.45.57 3.57a1 1 0 0 1-.25 1z"/></svg>
        555-018-4720
      </li>
      <li>
        <svg viewBox="0 0 24 24" aria-hidden="true"><path d="M2 5h20v14H2zm2 2v.5l8 5 8-5V7l-8 5z"/></svg>
        youremail@mailbox.com
      </li>
      <li>
        <svg viewBox="0 0 24 24" aria-hidden="true"><path d="M12 2a10 10 0 1 0 0 20 10 10 0 0 0 0-20zm0 3a7 7 0 1 1 0 14 7 7 0 0 1 0-14zm0 3a4 4 0 1 0 0 8 4 4 0 0 0 0-8z"/></svg>
        www.yourwebsite.com
      </li>
    </ul>
    <p class="address">Your address, city, state, ZIP 0000</p>
  </section>

  <section class="card back">
    <div class="brand">
      <span class="brand-square"></span>
      <span class="brand-name">K R Mortar</span>
    </div>
    <ul class="services">
      <li>Ready Mixed Concrete</li>
      <li>Bricks and Blocks</li>
      <li>Quarry Products- Gravel</li>
      <li>Aggregates</li>
      <li>Sand</li>
    </ul>
  </section>
</main>
</body>
</html>
```